Looking for an Innovative Print Design (Service Directory)

We need a new design for our advertisement within a printed colour services directory.

We are a compensation law firm called Velbrook Compensation Lawyers. Feel free to take a browse of our website www.velbrooklegal.com.au to get an idea of what we do and the kind of firm we are.

We are in the process of redeveloping our website and as such, so please don't adhere to the design principles of the current site- impress us with your originality!

On top of any editable formats, your final submissions must include a .pdf copy.
The same design will need to be presented in two dimensions:

- 154mm x 118mm (B1/B2 Half Page);
- 175mm x 113mm (B4 Half Page).

[For more information refer to attached Pdf.]

We have attached for you a few examples of other firms' designs (Sample1,2,3). These are by no means good, or what we're after, it's just to provide you with an idea of what sort of advertisements go into the service directory.

Hi all,

We want to emphasise that a priority of the design is that it must look:
• Professional
• Sophisticated
Please do not hesitate to use completely different colour schemes to the ones that are on our website- as we have said, our website will change in the near future, so cohesion between the current project and the website is not necessary!

Thanks!

Thank you for your submissions so far. There are some great ideas hidden in there. 

An issue we are having is that most of you are conforming to the same understanding of what it should look like. Remember that there is NO NEED to be bound by the image of firm as is. That is, feel free to use a different colour logo.

For inspiration, we relate well to the design aesthetics of: http://www.tinfernstudio.co.uk/

Look forward to seeing your 'out of the box' submissions. 

Reason: We've received a large amount of fantastic designs. However, what we're really looking for is something original. Please feel free to think outside the box (the final design doesn't need to look like a print ad), and construct a design that is completely incongruous with our website! While we do appreciate a minimalistic design, we have yet to receive something that really grabs your attention with its visuals. We're not sure but this may or may not be achieved with a full colour design. Thanks for all your submissions- they all have some features that really click with us. We look forward to the next wave of submissions!

Target Market(s)

We have various target markets, including mainly families, elderly people, blue collar workers.

These are individuals who are looking for assistance. They feel helpless or wronged.

Keep in mind that the people accessing these are those who prefer going to a printed directory rather than using a google search.

Industry/Entity Type

Law Firm

Font styles to use
Serif
Sans Serif

Requirements
Must have
• - Our name 'Velbrook Compensation Lawyers'
- Our logo (attached as logo.eps, logo.png, and logo.tif)
- Must include phone number as 1300 XXX XXX (this must be prominent)
- Must include the following service areas in these words: Motor vehicle claims, medical claims, superannuation claims, Workplace claims, negligence claims
- Our email address: info@velbrooklegal.com.au
- Our website address: www.velbrooklegal.com.au
- The following catchphrases: '98% success rate', and 'No win no fee' in those words
- Our location '412 Carvel Lane, Smithville, SYDNEY'
- For sizing dimensions, we need one in 154mm x 118mm and also a design in 175mm x 113mm (B4 Half Page) [refer to pdf attached]
Nice to have
• - Text indicating free initial consulatation
- Professional colour scheme
- As our website will be changed, do not worry about making the advertisement cohesive with our website design
- We want the design to be modern, but still professional
- Clean typeface
- No gradient colour scheme
- When designing, if you are looking to place more text onto the advertisement, these may be some considerations (feel free to change the wording): Accredited specialists, home and hospital visits

```html
<!DOCTYPE html>
<html lang="en">
<head>
<meta charset="utf-8">
<title>Velbrook Compensation Lawyers — Directory Advertisement</title>
<link rel="stylesheet" href="https://fonts.googleapis.com/css2?family=Cutive&family=Kameron:wght@700&display=swap">
<style>
  :root {
    --ink: #1c1c1c;
    --purple: #4a2a6c;
    --paper: #ffffff;
    --stone-light: #d9d9d9;
    --stone-mid: #9a9a9a;
    --rule: #2a2a2a;
  }
  * { margin: 0; padding: 0; box-sizing: border-box; }
  html, body { width: 1200px; height: 774px; overflow: hidden; background: var(--paper); }
  .ad {
    position: relative;
    width: 1200px;
    height: 774px;
    background: var(--paper);
    color: var(--ink);
    font-family: "Cutive", "Courier New", serif;
    overflow: hidden;
  }
  .corner-flag { position: absolute; top: 0; right: 0; width: 170px; height: 205px; }
  .corner-flag__text {
    position: absolute;
    top: 70px; right: -14px;
    transform: rotate(50deg);
    color: var(--paper);
    font-size: 17px;
    white-space: nowrap;
  }
  .hero-visual {
    position: absolute; left: 520px; top: 170px; width: 590px; height: 320px;
    background: radial-gradient(ellipse at 45% 45%, var(--stone-light) 0%, var(--stone-mid) 35%, var(--paper) 72%);
  }
  .headline { position: absolute; left: 93px; top: 88px; z-index: 1; }
  .headline__line { display: block; font-size: 35px; line-height: 47px; font-weight: 400; white-space: nowrap; }
  .headline__line--bold { font-family: "Kameron", Georgia, serif; font-weight: 700; font-size: 41px; }
  .headline__figure {
    display: block;
    font-family: "Kameron", Georgia, serif;
    font-weight: 700;
    color: var(--purple);
    font-size: 170px;
    line-height: 150px;
    letter-spacing: -4px;
    margin-top: 4px;
    margin-left: -5px;
  }
  .headline__line--tail { font-size: 34px; margin-top: 0; }
  .brand {
    position: absolute; left: 737px; top: 88px;
    display: flex; align-items: center; gap: 14px;
  }
  .brand__dot { width: 36px; height: 36px; border-radius: 50%; background: var(--ink); flex: none; }
  .brand__name { display: flex; flex-direction: column; color: var(--ink); text-transform: uppercase; }
  .brand__word { font-size: 24px; line-height: 26px; letter-spacing: 2px; }
  .brand__sub { font-size: 9px; line-height: 11px; letter-spacing: 1.7px; }
  .services { position: absolute; left: 88px; top: 488px; width: 1012px; }
  .services__title { font-family: "Kameron", Georgia, serif; font-weight: 700; font-size: 18px; margin-left: 2px; }
  .services__list {
    list-style: none;
    border-top: 1.5px solid var(--rule);
    border-bottom: 1.5px solid var(--rule);
    margin-top: 18px;
    padding: 15px 0 18px;
    display: grid;
    grid-template-columns: 290px 414px 1fr;
    row-gap: 6px;
    font-size: 17.5px;
    line-height: 20px;
  }
  .services__item { display: flex; align-items: center; gap: 8px; padding-left: 2px; white-space: nowrap; }
  .services__item::before {
    content: ""; width: 8px; height: 8px; border-radius: 50%; background: var(--purple); flex: none;
  }
  .services__item--wide::before { margin-right: 62px; }
  .contact { position: absolute; left: 90px; top: 631px; width: 1010px; }
  .contact__intro { font-size: 15px; }
  .contact__phone { display: flex; align-items: center; gap: 18px; margin-top: 8px; }
  .contact__phone-icon { width: 40px; height: 30px; }
  .contact__number {
    font-family: "Kameron", Georgia, serif; font-weight: 700;
    color: var(--purple); font-size: 40px; line-height: 40px; letter-spacing: 0;
  }
  .contact__details { display: flex; margin-top: 8px; font-size: 15px; white-space: nowrap; }
  .contact__detail--email { width: 340px; }
  .contact__detail--web { width: 315px; }
  .contact__label { font-family: "Kameron", Georgia, serif; font-weight: 700; color: var(--purple); margin-right: 4px; }
</style>
</head>
<body>
<main class="ad">
  <div class="corner-flag">
    <svg width="170" height="205" viewBox="0 0 170 205" aria-hidden="true">
      <polygon points="0,0 170,0 170,205" fill="var(--purple)"/>
    </svg>
    <span class="corner-flag__text">No Win, No Fee!</span>
  </div>

  <div class="hero-visual" role="img" aria-label="Grey pebbles balanced on a tilted flat stone like a set of scales"></div>

  <h1 class="headline">
    <span class="headline__line">EXPERIENCED</span>
    <span class="headline__line headline__line--bold">COMPENSATION</span>
    <span class="headline__line">LAWYERS WITH A:</span>
    <span class="headline__figure">98%</span>
    <span class="headline__line headline__line--tail">SUCCESS RATE</span>
  </h1>

  <div class="brand">
    <span class="brand__dot"></span>
    <span class="brand__name">
      <span class="brand__word">Velbrook</span>
      <span class="brand__sub">Compensation Lawyers</span>
    </span>
  </div>

  <section class="services">
    <h2 class="services__title">We can help you with:</h2>
    <ul class="services__list">
      <li class="services__item">Motor Vehicle Claims</li>
      <li class="services__item services__item--wide">Negligence Claims</li>
      <li class="services__item">Workplace Claims</li>
      <li class="services__item">Medical Claims</li>
      <li class="services__item services__item--wide">Superannuation Claims</li>
    </ul>
  </section>

  <section class="contact">
    <p class="contact__intro">For more information contact us on:</p>
    <div class="contact__phone">
      <svg class="contact__phone-icon" viewBox="0 0 40 30" aria-hidden="true">
        <path d="M2 10 C2 3 38 3 38 10 L38 13 L29 13 L29 9 L11 9 L11 13 L2 13 Z" fill="var(--purple)"/>
        <path d="M9 14 L31 14 L36 29 L4 29 Z" fill="var(--purple)"/>
        <circle cx="20" cy="21" r="4.5" fill="var(--paper)"/>
        <circle cx="20" cy="21" r="2" fill="var(--purple)"/>
      </svg>
      <span class="contact__number">1300 XXX XXX</span>
    </div>
    <div class="contact__details">
      <p class="contact__detail contact__detail--email"><span class="contact__label">E:</span> info@velbrooklegal.com.au</p>
      <p class="contact__detail contact__detail--web"><span class="contact__label">W:</span> www.velbrooklegal.com.au</p>
      <p class="contact__detail"><span class="contact__label">A:</span> 412 Carvel Lane, Smithville, Sydney</p>
    </div>
  </section>
</main>
</body>
</html>
```